Design for a Service-Based Estimate

We want a design for an Estimate that will always be sent in PDF format. The estimate or proposal is a critical document that needs to plainly show the service items, item description but also needs to be attractive and professional looking. Our current estimate deliverable is attached but it looks really basic like a Word document

```html
<!DOCTYPE html>
<html lang="en">
<head>
<meta charset="utf-8">
<title>Estimate – Firmbase Paving</title>
<link href="https://fonts.googleapis.com/css2?family=Poppins:wght@400;500;600;700&display=swap" rel="stylesheet">
<style>
  :root{
    --navy:#332f4f;
    --red:#e03a36;
    --ink:#1d1d24;
    --panel:#ededed;
    --rule:#d8d8d8;
    --bg:#e2e2e2;
    --paper:#ffffff;
  }
  *{margin:0;padding:0;box-sizing:border-box;}
  html,body{width:1200px;height:800px;overflow:hidden;}
  body{background:var(--bg);font-family:"Poppins",sans-serif;color:var(--ink);position:relative;}
  .page{position:absolute;background:var(--paper);overflow:hidden;box-shadow:0 2px 8px rgba(0,0,0,.18);}
  .page--estimate{left:169px;top:111px;width:406px;height:574px;}
  .page--terms{left:610px;top:109px;width:407px;height:576px;}
  .abs{position:absolute;}

  .brand{left:25px;top:28px;font-size:12.5px;font-weight:700;letter-spacing:.6px;color:var(--navy);display:flex;align-items:center;gap:5px;}
  .brand__dot{width:7px;height:7px;background:var(--red);}

  .recipient{right:27px;top:18px;text-align:right;font-size:7.5px;line-height:1.55;}
  .recipient__row{display:flex;justify-content:flex-end;align-items:center;gap:5px;}
  .recipient__gap{height:5px;}
  .icon{width:6px;height:7px;}

  .project{left:25px;top:100px;font-size:7.5px;line-height:1.55;}
  .project__title{font-weight:700;font-size:8px;text-transform:uppercase;margin-bottom:2px;}
  .project__underline{left:25px;top:140px;width:51px;height:2px;background:var(--red);}

  .meta{left:209px;top:103px;width:173px;height:33px;background:var(--panel);border-top:2px solid var(--navy);display:flex;}
  .meta__cell{flex:1;font-size:4.5px;text-align:center;padding-top:8px;text-transform:uppercase;}
  .meta__cell + .meta__cell{border-left:1px solid var(--rule);}

  .items{left:25px;top:197px;width:354px;}
  .items__rule{height:2px;background:var(--red);}
  .items__head{margin-top:1px;height:26px;background:var(--navy);color:#fff;display:flex;align-items:center;font-size:10px;}
  .items__body{height:232px;background:var(--panel);display:flex;border-bottom:1px solid var(--rule);}
  .col-item{width:177px;}
  .col-price{width:63px;}
  .col-qty{width:63px;}
  .col-total{flex:1;}
  .items__head > div{text-align:center;}
  .items__head .col-item{text-align:left;padding-left:65px;}
  .items__body > div + div{border-left:1px solid var(--rule);}

  .grand{left:240px;top:459px;width:114px;height:36px;background:var(--navy);border-bottom:2px solid var(--red);color:#fff;font-size:8px;font-weight:500;letter-spacing:.5px;padding:13px 0 0 20px;}

  .wave{left:0;bottom:0;width:100%;height:70px;}

  .terms__title{left:0;width:100%;top:24px;text-align:center;font-size:6.5px;font-weight:700;}
  .terms__body{left:22px;top:56px;width:366px;font-size:6.3px;line-height:12.3px;}
  .terms__list{list-style:none;}
  .terms__list li{position:relative;padding-left:6px;margin-bottom:12.3px;}
  .terms__list li::before{content:"";position:absolute;left:0;top:5px;width:2px;height:2px;border-radius:50%;background:var(--red);}
  .terms__note{padding-left:6px;}

  .sign{top:424px;width:118px;border-top:1px solid var(--ink);text-align:center;font-size:7px;padding-top:4px;}
  .sign--client{left:25px;}
  .sign--date{left:265px;}
</style>
</head>
<body>

<section class="page page--estimate">
  <div class="abs brand"><span>FIRMBASE PAVING</span><span class="brand__dot"></span></div>

  <div class="abs recipient">
    <div>To:</div>
    <div>Dale Morrow</div>
    <div class="recipient__gap"></div>
    <div class="recipient__row">418 Harbor Lane NE Tampa 33602
      <svg class="icon" viewBox="0 0 6 8"><path d="M3 7.5C1.5 5.5.5 4.2.5 3a2.5 2.5 0 0 1 5 0c0 1.2-1 2.5-2.5 4.5z" fill="none" stroke="#e03a36" stroke-width=".8"/><circle cx="3" cy="3" r=".8" fill="#e03a36"/></svg>
    </div>
    <div class="recipient__row">dmorrow@mailbox.com
      <svg class="icon" viewBox="0 0 6 7"><rect x="0" y="1.5" width="6" height="4.5" fill="#e03a36"/><path d="M0 1.5l3 2.4 3-2.4" fill="none" stroke="#fff" stroke-width=".6"/></svg>
    </div>
  </div>

  <div class="abs project">
    <div class="project__title">Dale Morrow New Concrete Pad</div>
    <div>418 Harbor Lane NE Tampa 33602</div>
    <div>Bid#: 24-0317</div>
  </div>
  <div class="abs project__underline"></div>

  <div class="abs meta">
    <div class="meta__cell">Estimate No:</div>
    <div class="meta__cell">Estimate Date :</div>
  </div>

  <div class="abs items">
    <div class="items__rule"></div>
    <div class="items__head">
      <div class="col-item">Item</div>
      <div class="col-price">Unit Price</div>
      <div class="col-qty">Quantity</div>
      <div class="col-total">Total</div>
    </div>
    <div class="items__body">
      <div class="col-item"></div>
      <div class="col-price"></div>
      <div class="col-qty"></div>
      <div class="col-total"></div>
    </div>
  </div>

  <div class="abs grand">TOTAL &nbsp;&nbsp;:</div>

  <svg class="abs wave" viewBox="0 504 406 70" preserveAspectRatio="none">
    <path d="M0 553 C70 540 160 548 250 562 C330 574 385 562 406 514 L406 574 L0 574Z" fill="var(--red)"/>
    <path d="M0 570 C80 550 170 558 260 570 C330 580 385 574 406 540 L406 574 L0 574Z" fill="var(--navy)"/>
  </svg>
</section>

<section class="page page--terms">
  <h1 class="abs terms__title">TERMS AND CONDITIONS</h1>
  <div class="abs terms__body">
    <ul class="terms__list">
      <li>Price as quoted in this estimate are valid for (60) days only.</li>
      <li>Payment in full, less any previously paid amounts, is due to the Contractor upon completion of the proposed scope of work.</li>
      <li>All change order requests must be communicated in writing to the Contractor by the client or their authorized representative.</li>
      <li>All measurements listed in this estimate are approximate and may vary slightly due to actual field conditions.</li>
      <li>It is agreed by the Contractor and the Client that complications and costs arising from unforeseen conditions and handling of unsuitable materials are not included in this estimate.</li>
      <li>Unless specifically listed in this estimate, thefollowing items and their costs are not included: Maintenance of Traffic, Concrete Material Pumping, Testing, Excavation, Grading &nbsp;and Fill Material, Permits and Fees, Surveying and As-Builts, Lrrigation repair, landscaping and Root Mitagation, De-watering, Private Locates and Accessibility.</li>
    </ul>
    <p class="terms__note">Private utility locating services using radio detection devices and, when necessary, ground penetrating radar are offered by Firmbase Paving to assist in finding private utilities that may not have been located by the public one call system. Firmbase Paving will not be responsible for private utilities that have not been located nor for the failure of the above equipment to accurately detect existing utilities since the equipment is fallible and existing site conditions may preclude the ability of the equipment to detect an identifiable signal.</p>
  </div>

  <div class="abs sign sign--client">Client Signature</div>
  <div class="abs sign sign--date">Date</div>

  <svg class="abs wave" viewBox="0 504 406 70" preserveAspectRatio="none">
    <path d="M0 553 C70 540 160 548 250 562 C330 574 385 562 406 514 L406 574 L0 574Z" fill="var(--red)"/>
    <path d="M0 570 C80 550 170 558 260 570 C330 580 385 574 406 540 L406 574 L0 574Z" fill="var(--navy)"/>
  </svg>
</section>

</body>
</html>
```